Design of a carbonated cola drink

our competitor is selling brimhaven cola
their design is en closed
we need a similar design colours but we cant use
brimhaven cola
we were thinking of usuing
the words VRO cola
using a bit of the american flag colors red and blue
designs for three flavors shown below should be shown
the main drink colour is zimp red
orange lurvo orange
punch like brevoni /glimmer fizz

Target Market(s)

pacific islands

Requirements
Must have
• mentioned above
Nice to have
• mentioned above

```html
<!DOCTYPE html>
<html lang="en">
<head>
<meta charset="utf-8">
<title>VRO Cola – Can Labels</title>
<link rel="stylesheet" href="https://fonts.googleapis.com/css2?family=Lilita+One&family=Pacifico&family=Roboto:wght@400;700&display=swap">
<style>
  :root {
    --bg: #f4f4f4;
    --punch: #7cc31f;
    --punch-light: #b8dc2a;
    --cola: #e3161f;
    --cola-light: #ef3a3f;
    --orange: #f26c14;
    --orange-light: #f79a2a;
    --navy: #1f3f8c;
    --white: #ffffff;
  }
  html, body {
    margin: 0;
    padding: 0;
    width: 1200px;
    height: 1200px;
    overflow: hidden;
    background: var(--bg);
  }
  .range {
    width: 1200px;
    height: 1200px;
    display: flex;
    align-items: center;
    justify-content: center;
    gap: 40px;
  }
  .label { display: block; box-shadow: 0 18px 40px rgba(0,0,0,0.15); }
  .label--side { width: 260px; height: 504px; }
  .label--main { width: 320px; height: 620px; }
  .label__ground { fill: var(--flavour); }
  .label__stripe { fill: var(--flavour-light); }
  .label__band { fill: var(--navy); }
  .label__brand {
    font-family: "Lilita One", sans-serif;
    font-size: 110px;
    fill: var(--white);
  }
  .label__flavour {
    font-family: "Pacifico", cursive;
    font-size: 40px;
    fill: var(--white);
  }
  .label__volume {
    font-family: "Roboto", sans-serif;
    font-size: 22px;
    fill: var(--white);
  }
  .badge__shape { fill: none; stroke: var(--white); stroke-width: 2.5; }
  .badge__caption { font-family: "Roboto", sans-serif; font-size: 6px; font-weight: 700; fill: var(--white); }
  .badge__value { font-family: "Roboto", sans-serif; font-size: 15px; font-weight: 700; fill: var(--white); }
  .label--punch { --flavour: var(--punch); --flavour-light: var(--punch-light); }
  .label--cola { --flavour: var(--cola); --flavour-light: var(--cola-light); }
  .label--orange { --flavour: var(--orange); --flavour-light: var(--orange-light); }
</style>
</head>
<body>
<main class="range">
  <svg class="label label--side label--punch" viewBox="0 0 320 620" role="img" aria-label="VRO Punch can label">
    <rect class="label__ground" width="320" height="620"/>
    <polygon class="label__stripe" points="0,430 320,340 320,390 0,480"/>
    <polygon class="label__band" points="0,480 320,390 320,450 0,540"/>
    <g class="badge" transform="translate(272,70)">
      <rect class="badge__shape" x="-16" y="-16" width="32" height="34" rx="10"/>
      <text class="badge__caption" x="0" y="-6" text-anchor="middle">CALORIES</text>
      <text class="badge__value" x="0" y="11" text-anchor="middle">110</text>
    </g>
    <text class="label__brand" x="160" y="230" text-anchor="middle">VRO</text>
    <text class="label__flavour" x="160" y="300" text-anchor="middle">Punch</text>
    <text class="label__volume" x="305" y="595" text-anchor="end">250ml</text>
  </svg>

  <svg class="label label--main label--cola" viewBox="0 0 320 620" role="img" aria-label="VRO Cola can label">
    <rect class="label__ground" width="320" height="620"/>
    <polygon class="label__band" points="0,480 320,390 320,450 0,540"/>
    <g class="badge" transform="translate(272,70)">
      <rect class="badge__shape" x="-16" y="-16" width="32" height="34" rx="10"/>
      <text class="badge__caption" x="0" y="-6" text-anchor="middle">CALORIES</text>
      <text class="badge__value" x="0" y="11" text-anchor="middle">110</text>
    </g>
    <text class="label__brand" x="160" y="230" text-anchor="middle">VRO</text>
    <text class="label__flavour" x="160" y="300" text-anchor="middle">Cola</text>
    <text class="label__volume" x="305" y="595" text-anchor="end">250ml</text>
  </svg>

  <svg class="label label--side label--orange" viewBox="0 0 320 620" role="img" aria-label="VRO Orange can label">
    <rect class="label__ground" width="320" height="620"/>
    <polygon class="label__stripe" points="0,430 320,340 320,390 0,480"/>
    <polygon class="label__band" points="0,480 320,390 320,450 0,540"/>
    <g class="badge" transform="translate(272,70)">
      <rect class="badge__shape" x="-16" y="-16" width="32" height="34" rx="10"/>
      <text class="badge__caption" x="0" y="-6" text-anchor="middle">CALORIES</text>
      <text class="badge__value" x="0" y="11" text-anchor="middle">110</text>
    </g>
    <text class="label__brand" x="160" y="230" text-anchor="middle">VRO</text>
    <text class="label__flavour" x="160" y="300" text-anchor="middle">Orange</text>
    <text class="label__volume" x="305" y="595" text-anchor="end">250ml</text>
  </svg>
</main>
</body>
</html>
```